Fresh Nest Builder Guide needs a new Landing Page

I like to get a landing page or website with 2-3 pages to help target home buyers who are looking to buy homes from builders such as PV Dwellings, Moritz, G.T. Falwick, etc. The landing page/website to be non-cluttered and be able to explain to home buyers that there are many benefits to include me as their buyer's agent when they buy a brand new home from any builders.
I may want to incorporate a short explanation video (animated) on the landing page and then for the viewer to click on a button that will take them to another page where they can search for new homes from different builders.
Target Market(s)
Home buyers looking to buy brand new home from builders such as PV Dwellings, Moritz, G.T. Falwick, etc.
Industry/Entity Type
Real Estate
Number of Pages Required
2 page
Requirements
Must have
- The landing page may have the explanation video at the bottom of the landing page (scrolled down) or there may be a CALL TO ACTION button that takes the viewer to the 2nd page to watch the explanation video. Once they watched the explanation video and are still interested, they can click on another CALL TO ACTION button that will take them to another website that they will be able to search for all the available new homes and register their contact information.
Should not have
- No clutters and no dark colors.

```html
<!DOCTYPE html>
<html lang="en">
<head>
<meta charset="utf-8">
<title>Fresh Nest Builder Guide</title>
<link rel="stylesheet" href="https://fonts.googleapis.com/css2?family=Montserrat:wght@400;500;600;700&display=swap">
<style>
  :root {
    --ink-white: #ffffff;
    --ink-soft: rgba(255,255,255,0.94);
    --wall-shadow: #8e9196;
    --wall-mid: #adb0b4;
    --wall-light: #c9cbce;
    --floor: #7f7d80;
    --shade-left: rgba(48,52,58,0.42);
    --shade-right: rgba(48,52,58,0.12);
    --accent-top: #ea6e2f;
    --accent-bottom: #d4531f;
    --rule: rgba(255,255,255,0.45);
    --play-ring: rgba(255,255,255,0.4);
    --play-inner: rgba(255,255,255,0.65);
    --play-core: #5b5d61;
  }
  * { margin: 0; padding: 0; box-sizing: border-box; }
  html, body { width: 1200px; height: 648px; overflow: hidden; }
  body { font-family: "Montserrat", sans-serif; color: var(--ink-white); background: var(--wall-mid); }

  .landing { position: relative; width: 1200px; height: 648px; overflow: hidden; }

  .hero-photo {
    position: absolute; inset: 0;
    background:
      linear-gradient(180deg, transparent 0%, transparent 72%, var(--floor) 92%),
      linear-gradient(100deg, var(--wall-shadow) 0%, var(--wall-mid) 30%, var(--wall-light) 58%, var(--wall-mid) 84%, var(--wall-shadow) 100%);
  }
  .hero-shade { position: absolute; inset: 0; background: linear-gradient(90deg, var(--shade-left) 0%, var(--shade-left) 40%, var(--shade-right) 75%); }

  .brand {
    position: absolute; left: 99px; top: 18px; width: 178px;
    display: flex; flex-direction: column; align-items: center; gap: 8px;
  }
  .brand-dot { width: 24px; height: 24px; border-radius: 50%; background: var(--ink-white); }
  .brand-name { font-size: 19px; font-weight: 500; line-height: 1.1; text-align: center; color: var(--ink-white); }

  .top-bar {
    position: absolute; right: 100px; top: 28px;
    display: flex; align-items: center; gap: 20px;
  }
  .phone { display: flex; align-items: center; gap: 10px; font-size: 16px; font-weight: 700; letter-spacing: 2px; color: var(--ink-soft); }
  .menu-icon { display: block; }

  .hero-copy { position: absolute; left: 93px; top: 206px; width: 640px; }
  .hero-title { font-size: 64px; font-weight: 600; line-height: 0.98; letter-spacing: 0.5px; }
  .hero-lede { margin-top: 18px; padding-left: 6px; font-size: 21px; font-weight: 400; line-height: 37px; color: var(--ink-soft); }

  .cta {
    position: absolute; left: 99px; top: 437px; width: 180px; height: 51px;
    border-radius: 26px;
    background: linear-gradient(180deg, var(--accent-top), var(--accent-bottom));
    color: var(--ink-white); font-size: 16px; font-weight: 700; letter-spacing: 0.5px;
    display: flex; align-items: center; justify-content: center; text-decoration: none;
  }

  .play-video { position: absolute; left: 855px; top: 247px; }

  .site-footer {
    position: absolute; left: 0; right: 0; top: 590px; height: 58px;
    border-top: 1px solid var(--rule);
  }
  .legal { position: absolute; left: 102px; top: 21px; font-size: 14px; color: var(--ink-soft); }
  .legal a { color: var(--ink-soft); text-decoration: none; }
  .social { position: absolute; left: 962px; top: 21px; display: flex; gap: 22px; list-style: none; }
  .social li { width: 18px; height: 18px; border-radius: 50%; background: var(--ink-white); }
</style>
</head>
<body>
<main class="landing">
  <div class="hero-photo" role="img" aria-label="Bright modern living room with grey sofa, lounge chairs, pendant lamps and a window"></div>
  <div class="hero-shade"></div>

  <header>
    <div class="brand">
      <span class="brand-dot"></span>
      <span class="brand-name">Fresh Nest<br>Builder Guide</span>
    </div>
    <div class="top-bar">
      <span class="phone">
        <svg width="16" height="16" viewBox="0 0 24 24" aria-hidden="true"><path fill="currentColor" d="M6.6 10.8a15.1 15.1 0 0 0 6.6 6.6l2.2-2.2a1 1 0 0 1 1-.25 11.4 11.4 0 0 0 3.6.57 1 1 0 0 1 1 1V20a1 1 0 0 1-1 1A17 17 0 0 1 3 4a1 1 0 0 1 1-1h3.5a1 1 0 0 1 1 1c0 1.25.2 2.45.57 3.57a1 1 0 0 1-.25 1z"/></svg>
        Ph:555-204-7316
      </span>
      <svg class="menu-icon" width="22" height="16" viewBox="0 0 22 16" aria-label="Menu"><rect y="0" width="22" height="3.5" rx="1.7" fill="#fff"/><rect y="6.2" width="22" height="3.5" rx="1.7" fill="#fff"/><rect y="12.5" width="22" height="3.5" rx="1.7" fill="#fff"/></svg>
    </div>
  </header>

  <section class="hero-copy">
    <h1 class="hero-title">Fresh Nest<br>Builder Guide</h1>
    <p class="hero-lede">Lorem ipsum dolor sit ameconctetur<br>adipiscing elit, sed do eiusmo.</p>
  </section>

  <a class="cta" href="#">GET STARTED</a>

  <svg class="play-video" width="136" height="136" viewBox="0 0 136 136" aria-label="Play video">
    <circle cx="68" cy="68" r="68" fill="var(--play-ring)"/>
    <circle cx="68" cy="68" r="57" fill="var(--play-inner)"/>
    <circle cx="68" cy="68" r="41" fill="var(--play-core)"/>
    <path d="M59 52 L82 68 L59 84 Z" fill="#fff"/>
  </svg>

  <footer class="site-footer">
    <p class="legal">© 2018 All Rights are Reserved. <a href="#">Privacy Policy</a> | <a href="#">Terms of Use</a> | <a href="#">Contact</a></p>
    <ul class="social" aria-label="Social links">
      <li></li><li></li><li></li><li></li>
    </ul>
  </footer>
</main>
</body>
</html>
```